New career and executive coaching business needs a business card design including logo

Company name: 'Harbourline Career Partners.' The aim of my coaching engagements is to help people improve their communication in the workplace and achieve their career goals. The process involves working with individuals to help them uncover their strengths and talents, then leverage those to improve their working lives. The Tellwood Inventory is the starting point to the process. I am after an exciting and interesting business card design (including logo)which is professional yet will still get people's attention.

Industry/Entity Type

Business

Contact Information for Business Card

Name: Gavin Holloway
Position: Owner
Address: 58 Pellimore Cres, Wardell Vic 3197
Phone: 0481937145
Website: harbourlinecareer.com.au
Email: gavin@hcp.com.au

Colors
33a6d7
00a990
0355a3
3176b5

Requirements
Must have
• logo

```html
<!DOCTYPE html>
<html lang="en">
<head>
<meta charset="utf-8">
<title>Harbourline Career Partners – Business Card</title>
<link rel="stylesheet" href="https://fonts.googleapis.com/css2?family=Questrial&family=Arimo:wght@400&display=swap">
<style>
  :root {
    --blue: #33a6d7;
    --ink: #2b2b2b;
    --black-top: #2c2c2c;
    --black-bottom: #0c0c0c;
    --grey-light: #dcdddf;
    --grey-mid: #b5b7ba;
    --grey-dark: #8d9094;
    --white: #ffffff;
    --stage: #e7e4df;
    --base: #ffffff;
  }
  html, body {
    margin: 0;
    padding: 0;
    width: 1200px;
    height: 2290px;
    overflow: hidden;
    background: var(--base);
  }
  .canvas {
    position: relative;
    width: 1200px;
    height: 2290px;
  }
  .card-stage {
    position: absolute;
    left: 0;
    width: 1200px;
    height: 900px;
    background: var(--stage);
    display: flex;
    align-items: center;
    justify-content: center;
  }
  .card-stage--front { top: 0; }
  .card-stage--back { top: 900px; }
  .card {
    width: 1000px;
    height: 571px;
    display: block;
    filter: drop-shadow(0 18px 28px rgba(0,0,0,0.22));
  }
  .brand-name {
    font-family: "Questrial", sans-serif;
    fill: var(--blue);
  }
  .holder-name {
    font-family: "Arimo", sans-serif;
    fill: var(--ink);
  }
  .holder-role {
    font-family: "Arimo", sans-serif;
    fill: var(--blue);
  }
  .contact-text {
    font-family: "Arimo", sans-serif;
    fill: var(--white);
  }
  .web-text {
    font-family: "Arimo", sans-serif;
    fill: var(--blue);
  }
  .logo-lockup {
    position: absolute;
    top: 1800px;
    left: 0;
    width: 1200px;
    height: 490px;
    display: flex;
    align-items: center;
    justify-content: center;
    gap: 28px;
  }
  .logo-lockup__dot {
    width: 64px;
    height: 64px;
    border-radius: 50%;
    background: var(--grey-dark);
  }
  .logo-lockup__name {
    font-family: "Questrial", sans-serif;
    font-size: 60px;
    color: var(--blue);
    letter-spacing: 1px;
  }
</style>
</head>
<body>
<main class="canvas">

  <section class="card-stage card-stage--front">
    <svg class="card card--front" viewBox="0 0 1000 571" xmlns="http://www.w3.org/2000/svg">
      <defs>
        <clipPath id="front-shape"><rect width="1000" height="571" rx="28"/></clipPath>
        <linearGradient id="front-dark" x1="0" y1="0" x2="0" y2="1">
          <stop offset="0" stop-color="var(--black-top)"/>
          <stop offset="1" stop-color="var(--black-bottom)"/>
        </linearGradient>
        <linearGradient id="front-grey" x1="0" y1="0" x2="0" y2="1">
          <stop offset="0" stop-color="var(--grey-light)"/>
          <stop offset="1" stop-color="var(--grey-mid)"/>
        </linearGradient>
      </defs>
      <g clip-path="url(#front-shape)">
        <rect class="front-base" width="1000" height="571" fill="url(#front-grey)"/>
        <rect class="front-dark-panel" width="1000" height="300" fill="url(#front-dark)"/>
        <rect class="front-divider" y="300" width="1000" height="6" fill="#f4f4f4"/>
        <rect class="front-contact-band" y="468" width="1000" height="46" fill="var(--blue)"/>
      </g>

      <circle class="brand-dot" cx="88" cy="156" r="18" fill="var(--grey-dark)"/>
      <text class="brand-name" x="122" y="171" font-size="44">Harbourline Career Partners</text>

      <text class="holder-name" x="940" y="390" font-size="40" text-anchor="end">Gavin Holloway</text>
      <text class="holder-role" x="940" y="426" font-size="20" text-anchor="end">Owner</text>

      <g class="contact-row">
        <path class="icon-pin" d="M46 478c-6 0-11 5-11 11 0 8 11 18 11 18s11-10 11-18c0-6-5-11-11-11zm0 15a4 4 0 1 1 0-8 4 4 0 0 1 0 8z" fill="var(--white)"/>
        <text class="contact-text" x="66" y="498" font-size="19">58 Pellimore Cres, Wardell Vic 3197</text>

        <path class="icon-phone" d="M476 482h18a3 3 0 0 1 3 3v3h-6l-2-3h-8l-2 3h-6v-3a3 3 0 0 1 3-3zm-2 9h22l2 12h-26z" fill="var(--white)"/>
        <text class="contact-text" x="508" y="498" font-size="19">0481937145</text>

        <g class="icon-mail">
          <rect x="684" y="483" width="24" height="16" fill="var(--white)"/>
          <path d="M684 483l12 9 12-9" fill="none" stroke="var(--blue)" stroke-width="2"/>
        </g>
        <text class="contact-text" x="718" y="498" font-size="19">gavin@hcp.com.au</text>
      </g>
    </svg>
  </section>

  <section class="card-stage card-stage--back">
    <svg class="card card--back" viewBox="0 0 1000 571" xmlns="http://www.w3.org/2000/svg">
      <defs>
        <clipPath id="back-shape"><rect width="1000" height="571" rx="28"/></clipPath>
        <linearGradient id="back-white" x1="0" y1="0" x2="1" y2="1">
          <stop offset="0" stop-color="#ffffff"/>
          <stop offset="1" stop-color="#eeeeef"/>
        </linearGradient>
        <linearGradient id="back-grey" x1="0" y1="0" x2="1" y2="0">
          <stop offset="0" stop-color="var(--grey-light)"/>
          <stop offset="1" stop-color="var(--grey-dark)"/>
        </linearGradient>
      </defs>
      <g clip-path="url(#back-shape)">
        <rect class="back-base" width="1000" height="571" fill="url(#back-white)"/>
        <path class="back-swoosh" d="M0 500C520 480 860 360 900 0H1000V571H0Z" fill="var(--blue)"/>
        <path class="back-swoosh-gap" d="M0 540C540 520 890 375 938 0H1000V571H0Z" fill="#ffffff"/>
        <path class="back-grey-panel" d="M0 550C548 530 900 380 950 0H1000V571H0Z" fill="url(#back-grey)"/>
      </g>

      <circle class="brand-dot" cx="96" cy="226" r="18" fill="var(--grey-dark)"/>
      <text class="brand-name" x="130" y="241" font-size="44">Harbourline Career Partners</text>

      <text class="web-text" x="290" y="335" font-size="22">harbourlinecareer.com.au</text>
    </svg>
  </section>

  <section class="logo-lockup">
    <span class="logo-lockup__dot"></span>
    <span class="logo-lockup__name">Harbourline Career Partners</span>
  </section>

</main>
</body>
</html>
```